Business Card Design Project Bright Way

Simple and clean business card,

Logo and fond added in attachment

Data need to be changable:
Lien Varmeko
Customer Service Specialist

Bright Way - lien.varmeko@brightway-mail.be - Mob: +32471538046 - www.brightway-mail.be

Target Market(s)

Small businesses

Industry/Entity Type

Business

Requirements
Nice to have
• QR-code

```html
<!DOCTYPE html>
<html lang="en">
<head>
<meta charset="utf-8">
<title>Bright Way – Business Card</title>
<link rel="stylesheet" href="https://fonts.googleapis.com/css2?family=Mulish:ital,wght@0,400;0,800;1,400;1,800&display=swap">
<style>
  :root {
    --backdrop: #2f3b42;
    --card: #ffffff;
    --ink: #1b1b1b;
    --brand-blue: #0aa2dc;
    --brand-green: #7cc242;
  }
  * { margin: 0; padding: 0; box-sizing: border-box; }
  html, body {
    width: 1200px;
    height: 900px;
    overflow: hidden;
    background: var(--backdrop);
    font-family: "Mulish", sans-serif;
  }
  .card {
    position: absolute;
    left: 150px;
    top: 170px;
    width: 900px;
    height: 560px;
    background: var(--card);
    overflow: hidden;
  }
  .brand {
    position: absolute;
    right: 70px;
    top: 52px;
    display: flex;
    align-items: center;
    gap: 14px;
  }
  .brand-mark {
    width: 46px;
    height: 46px;
    background: var(--brand-blue);
  }
  .brand-name {
    font-size: 52px;
    font-weight: 800;
    color: var(--brand-green);
    line-height: 1;
  }
  .holder {
    position: absolute;
    left: 100px;
    top: 150px;
  }
  .holder-name {
    font-size: 34px;
    font-weight: 800;
    font-style: italic;
    color: var(--ink);
  }
  .holder-role {
    font-size: 23px;
    font-style: italic;
    color: var(--ink);
    margin-top: 2px;
  }
  .contacts {
    position: absolute;
    left: 100px;
    top: 290px;
    list-style: none;
  }
  .contact {
    display: flex;
    align-items: center;
    gap: 12px;
    font-size: 24px;
    font-style: italic;
    color: var(--ink);
    height: 38px;
  }
  .contact svg { width: 20px; height: 20px; fill: var(--brand-blue); flex: none; }
  .stripes { position: absolute; left: 0; bottom: 0; width: 100%; }
  .stripe-thin { height: 5px; background: var(--brand-blue); }
  .stripe-gap { height: 4px; background: var(--card); }
  .stripe-green { height: 11px; background: var(--brand-green); }
  .stripe-band { height: 82px; background: var(--brand-blue); }
</style>
</head>
<body>
  <article class="card">
    <div class="brand">
      <span class="brand-mark"></span>
      <span class="brand-name">Bright Way</span>
    </div>

    <div class="holder">
      <h1 class="holder-name">Lien Varmeko</h1>
      <p class="holder-role">Customer Service Specialist</p>
    </div>

    <ul class="contacts">
      <li class="contact">
        <svg viewBox="0 0 24 24" aria-hidden="true"><path d="M6.6 10.8a15.1 15.1 0 0 0 6.6 6.6l2.2-2.2c.3-.3.7-.4 1-.2 1.1.4 2.3.6 3.6.6.6 0 1 .4 1 1V20c0 .6-.4 1-1 1A17 17 0 0 1 3 4c0-.6.4-1 1-1h3.5c.6 0 1 .4 1 1 0 1.3.2 2.5.6 3.6.1.3 0 .7-.2 1z"/></svg>
        +32471538046
      </li>
      <li class="contact">
        <svg viewBox="0 0 24 24" aria-hidden="true"><path d="M2 8l10 6 10-6v11H2z"/><path d="M2 7l10-5 10 5-10 6z"/></svg>
        lien.varmeko@brightway-mail.be
      </li>
      <li class="contact">
        <svg viewBox="0 0 24 24" aria-hidden="true"><circle cx="12" cy="12" r="10"/><path d="M2 12h20M12 2c3 3 3 17 0 20M12 2c-3 3-3 17 0 20" stroke="#fff" stroke-width="1.4" fill="none"/></svg>
        www.brightway-mail.be
      </li>
    </ul>

    <div class="stripes">
      <div class="stripe-thin"></div>
      <div class="stripe-gap"></div>
      <div class="stripe-green"></div>
      <div class="stripe-gap"></div>
      <div class="stripe-gap"></div>
      <div class="stripe-band"></div>
    </div>
  </article>
</body>
</html>
```